Bref créative
Business Cards and Stationary for Real Estate Firm
Maple Crest Realty Group
Professional
Dennis R. Holloway
Broker/Owner
4782 Lantern Hill Rd
Suite 308
Petaluma, CA 95862
dholloway@brightharborfirm.com
www.maplecrestrealtygroup.net
DRE # 02947716
There should be a place for a photo of the agent on the front of the card, but can work fine if the agent does not put their photo on it. These card designs will be used for multiple agents, I assume the name, phone numbers, email address, etc can be changed for each agent. The AI files and any others that may be needed are in the uploaded zip file.
The back of the card may be a tag line or some other kind of message.
Files in black and white, and with color.

```html
<!DOCTYPE html>
<html lang="en">
<head>
<meta charset="utf-8">
<title>Maple Crest Realty Group — Stationery Set</title>
<link href="https://fonts.googleapis.com/css2?family=Playfair+Display:wght@400;700&family=Lato:wght@400;700&display=swap" rel="stylesheet">
<style>
:root{
  --bg-top:#f4f4f4;
  --bg-bottom:#dcdcdc;
  --red:#d0141f;
  --red-dark:#9e0c14;
  --red-light:#ee3a41;
  --paper:#ffffff;
  --ink:#555555;
  --grey-card:#e6e6e6;
  --shadow:0 1px 3px rgba(0,0,0,.25);
}
*{box-sizing:border-box;margin:0;padding:0}
html,body{width:1200px;height:247px;overflow:hidden}
body{background:linear-gradient(var(--bg-top),var(--bg-bottom));font-family:"Lato",sans-serif;color:var(--ink);position:relative}
.item{position:absolute;box-shadow:var(--shadow);overflow:hidden}
.wave{position:absolute;left:0;width:100%}
.brand{font-family:"Playfair Display",serif;font-weight:700;line-height:1.05;text-align:center;display:flex;align-items:center;gap:2px;justify-content:center}
.brand .dot{width:4px;height:4px;border-radius:50%;background:currentColor;flex:none}
.brand--red{color:var(--red)}
.brand--white{color:#fff}
.tagline{font-size:3px;text-align:center;color:var(--ink);letter-spacing:.2px}
.card{width:80px;height:52px}
.card--red{background:linear-gradient(135deg,var(--red-light),var(--red-dark))}
.card--white{background:var(--paper)}
.card--grey{background:var(--grey-card)}
.card .brand{font-size:5px;margin-top:16px}
.contact{position:absolute;left:6px;bottom:5px;font-size:2.4px;line-height:1.35}
.contact .name{font-family:"Playfair Display",serif;font-weight:700;font-size:3.6px;color:var(--red)}
.photo-slot{position:absolute;left:6px;top:18px;width:20px;height:26px;background:linear-gradient(#cfcfcf,#b5b5b5)}
.roof-art{position:absolute;left:4px;bottom:4px;width:38px;height:22px;background:linear-gradient(var(--red-light),var(--red))}
.letterhead{width:96px;height:228px;background:var(--paper)}
.letterhead .brand{font-size:6px;position:absolute;top:14px;left:0;right:0}
.letter-body{position:absolute;left:10px;right:10px;top:48px;font-size:2.6px;line-height:1.6}
.signature{position:absolute;left:10px;top:150px;font-family:"Playfair Display",serif;font-size:5px;color:#333}
.letter-foot{position:absolute;left:0;right:0;bottom:6px;font-size:2.2px;text-align:center;color:#fff}
.envelope{background:var(--paper)}
.envelope .brand{font-size:4px;position:absolute;left:6px;top:6px}
.envelope--red{background:linear-gradient(var(--red-light),var(--red-dark))}
.folder-inside{width:390px;height:200px;background:var(--paper)}
.folder-panel{position:absolute;top:0;height:100%;width:195px}
.folder-panel--left{left:0;background:linear-gradient(135deg,var(--red-light),var(--red-dark))}
.folder-panel--right{left:195px;background:#f7f7f7}
.pocket{position:absolute;bottom:0;left:0;width:100%;height:80px;background:var(--red)}
.pocket--white{background:var(--paper);border-top:1px solid #ddd}
.folder-cover{width:100px;height:190px;background:linear-gradient(135deg,var(--red-light),var(--red-dark))}
.folder-cover .brand{font-size:6px;margin-top:40px}
</style>
</head>
<body>

<!-- Business cards -->
<div class="item card card--red" style="left:80px;top:72px">
  <div class="brand brand--white"><span class="dot"></span>Maple Crest Realty Group</div>
</div>
<div class="item card card--white" style="left:165px;top:72px">
  <div class="photo-slot" role="img" aria-label="Agent photo placeholder"></div>
  <div class="contact" style="left:30px">
    <div class="name">Dennis R. Holloway</div>
    <div>Broker/Owner · DRE # 02947716</div>
    <div>4782 Lantern Hill Rd, Suite 308</div>
    <div>Petaluma, CA 95862</div>
    <div>(707) 555-0148</div>
    <div>dholloway@brightharborfirm.com</div>
    <div>www.maplecrestrealtygroup.net</div>
  </div>
</div>
<div class="item card card--grey" style="left:80px;top:140px">
  <div class="roof-art" role="img" aria-label="Red house roof illustration"></div>
  <div class="brand brand--red" style="font-size:4px;position:absolute;right:4px;top:14px;width:34px">Maple Crest Realty Group</div>
</div>
<div class="item card card--white" style="left:165px;top:140px">
  <div class="brand brand--red"><span class="dot"></span>Maple Crest Realty Group</div>
  <div class="tagline">Trusted Local Experts</div>
</div>

<!-- Letterheads -->
<div class="item letterhead" style="left:250px;top:10px">
  <svg class="wave" style="top:0" viewBox="0 0 96 12" height="12"><path d="M0 0H96V6Q60 14 30 6T0 8Z" fill="var(--red)"/></svg>
  <div class="brand brand--red"><span class="dot"></span>Maple Crest Realty Group</div>
  <p class="letter-body">Dear Client, thank you for choosing our team. We look forward to helping you find your next home.</p>
  <div class="signature">Sincerely,</div>
  <svg class="wave" style="bottom:0" viewBox="0 0 96 18" height="18"><path d="M0 6Q30 0 60 6T96 4V18H0Z" fill="var(--red)"/></svg>
  <div class="letter-foot">4782 Lantern Hill Rd, Suite 308 · Petaluma, CA 95862</div>
</div>
<div class="item letterhead" style="left:350px;top:10px">
  <svg class="wave" style="top:0" viewBox="0 0 96 12" height="12"><path d="M0 0H96V6Q60 14 30 6T0 8Z" fill="var(--red)"/></svg>
  <div class="brand brand--red"><span class="dot"></span>Maple Crest Realty Group</div>
  <p class="letter-body">Dear Client, thank you for choosing our team. We look forward to helping you find your next home.</p>
  <div class="signature">Sincerely,</div>
  <svg class="wave" style="bottom:0" viewBox="0 0 96 18" height="18"><path d="M0 6Q30 0 60 6T96 4V18H0Z" fill="var(--red)"/></svg>
  <div class="letter-foot">www.maplecrestrealtygroup.net</div>
</div>

<!-- Envelopes -->
<div class="item envelope" style="left:452px;top:122px;width:92px;height:46px">
  <div class="brand brand--red"><span class="dot"></span>Maple Crest Realty Group</div>
  <svg class="wave" style="bottom:0" viewBox="0 0 92 10" height="10"><path d="M0 4Q30 0 60 4T92 2V10H0Z" fill="var(--red)"/></svg>
</div>
<div class="item envelope envelope--red" style="left:550px;top:120px;width:94px;height:42px">
  <svg style="position:absolute;inset:0" viewBox="0 0 94 42"><path d="M0 0L47 24L94 0" fill="none" stroke="var(--red-dark)" stroke-width="1"/></svg>
</div>
<div class="item envelope" style="left:550px;top:166px;width:94px;height:40px">
  <div class="brand brand--red"><span class="dot"></span>Maple Crest Realty Group</div>
  <svg class="wave" style="bottom:0" viewBox="0 0 94 8" height="8"><path d="M0 4Q30 0 60 4T94 2V8H0Z" fill="var(--red)"/></svg>
</div>

<!-- Presentation folder -->
<div class="item folder-inside" style="left:655px;top:15px">
  <div class="folder-panel folder-panel--left"><div class="pocket" style="background:var(--red-dark)"></div></div>
  <div class="folder-panel folder-panel--right">
    <div class="brand brand--red" style="font-size:9px;margin-top:50px"><span class="dot"></span>Maple Crest Realty Group</div>
    <div class="pocket pocket--white"></div>
  </div>
</div>
<div class="item folder-cover" style="left:1065px;top:15px">
  <div class="brand brand--white"><span class="dot"></span>Maple Crest Realty Group</div>
</div>
<div class="item card card--white" style="left:1100px;top:188px;width:70px;height:20px">
  <div class="brand brand--red" style="font-size:3.5px;margin-top:7px">Maple Crest Realty Group</div>
</div>

</body>
</html>
```